Bluerock Data Partners - IT Support Tri-Fold

Need a tri-fold brochure for marketing, pitching managed IT Services. These services include computer/server management, security, cloud backups. The tri-fold should use our logo and colors (Attached)

```html
<!DOCTYPE html>
<html lang="en">
<head>
<meta charset="utf-8">
<title>Bluerock Data Partners – IT Services Tri-Fold</title>
<link href="https://fonts.googleapis.com/css2?family=Montserrat:ital,wght@0,300;0,400;0,500;0,700;0,800;1,800&display=swap" rel="stylesheet">
<style>
:root{
  --bg:#7a7a7a;
  --paper:#f2f2f2;
  --paper-shade:#dcdcdc;
  --navy:#13294d;
  --navy-deep:#0c1c38;
  --ink:#222;
  --tab-dark:#2a2a2a;
  --tab-gray:#6d6d6d;
  --rule:#9a9a9a;
  --accent:#3a4fa0;
  --white:#fff;
}
*{box-sizing:border-box;margin:0;padding:0}
html,body{width:1200px;height:795px;overflow:hidden}
body{background:var(--bg);font-family:"Montserrat",sans-serif;color:var(--ink);position:relative}

.spread{position:absolute;left:30px;top:72px;width:840px;height:650px;display:flex;box-shadow:0 10px 30px rgba(0,0,0,.35)}
.panel{width:280px;height:100%;position:relative;padding:38px 22px 0}
.panel--residential{background:linear-gradient(160deg,var(--paper) 0%,var(--paper-shade) 100%)}
.panel--business{background:linear-gradient(170deg,#1c3560 0%,var(--navy) 45%,var(--navy-deep) 100%);color:var(--white)}
.panel--web{background:linear-gradient(160deg,#f7f7f7 0%,var(--paper-shade) 100%)}

.heading{margin-bottom:16px}
.heading span{display:inline-block;font-weight:300;font-size:21px;letter-spacing:1px;color:var(--white);padding:3px 12px;line-height:1.1}
.heading .top{background:var(--tab-dark)}
.heading .bottom{background:var(--tab-gray);margin-left:14px;display:table}

.intro{font-size:8.4px;line-height:1.45;font-weight:400;margin-bottom:14px}
.panel--business .intro{color:#dbe2ee}

.price-list{list-style:none;font-size:9.6px}
.price-list li{display:flex;justify-content:space-between;border-bottom:1px solid var(--rule);padding:3px 4px;line-height:1.2}
.price-list li:first-child{border-top:1px solid var(--rule)}
.price-list .rate{font-weight:700;border-left:1px solid var(--rule);padding-left:8px;width:58px;text-align:right}
.panel--business .price-list li{border-color:rgba(255,255,255,.45)}
.panel--business .price-list .rate{border-color:rgba(255,255,255,.45)}

.clients{position:absolute;left:0;bottom:0;width:560px;height:78px;background:var(--white);border-top:3px solid var(--accent)}
.clients-tab{position:absolute;left:0;top:-20px;background:var(--accent);color:var(--white);font-size:9.5px;font-weight:700;padding:4px 14px}
.client-names{display:flex;flex-wrap:wrap;gap:6px 16px;padding:16px 16px 0;font-size:9px;font-weight:700;color:var(--navy)}
.client-names li{list-style:none}

.panel--web .intro{margin-bottom:12px}

.cover{position:absolute;left:900px;top:72px;width:280px;height:650px;background:var(--white);box-shadow:0 10px 30px rgba(0,0,0,.35);padding-top:30px}
.brand{text-align:center}
.brand-mark{display:inline-block;font-weight:800;font-size:34px;letter-spacing:10px;color:var(--navy)}
.brand-name{font-weight:700;font-size:13px;margin-top:4px;color:var(--ink)}
.cover-photo{display:block;margin-top:18px;width:280px;height:250px;background:linear-gradient(135deg,#c9d6e6 0%,#8ea4bd 45%,#3a4b5e 100%)}
.cover-title{margin:-60px 0 0 10px;position:relative}
.cover-title span{display:table;background:var(--tab-dark);color:var(--white);font-weight:800;font-style:italic;font-size:19px;padding:4px 12px;margin-bottom:6px}
.cover-title .mid{background:var(--tab-gray);margin-left:-4px}
.cover-sub{margin:14px 0 0 22px;font-size:10.5px;font-weight:300;letter-spacing:.5px;line-height:1.5;color:#444}
.cover-rule{width:14px;height:3px;background:var(--accent);margin:14px 0 0 22px}
.cover-url{margin:22px 0 0 22px;font-size:10.5px;letter-spacing:1.5px;color:#444}
.cover-url b{color:var(--accent);font-weight:700}
</style>
</head>
<body>

<section class="spread">
  <article class="panel panel--residential">
    <h2 class="heading"><span class="top">RESIDENTIAL</span><span class="bottom">SERVICES</span></h2>
    <p class="intro">From the simplest task to the most complex, let Bluerock service all of your residential tech needs. We work with transparent, one-time rates and travel on-site to CT, RI and MA. If you are outside of this area, we can remote into your computer to fix many issues. We are happy to provide additional services that aren't listed, please call for information!</p>
    <ul class="price-list">
      <li><span>Wifi/wired Network Install &amp; Setup</span><span class="rate">$100/hr</span></li>
      <li><span>Tune Up</span><span class="rate">$100/hr</span></li>
      <li><span>Virus Removal</span><span class="rate">$100/hr</span></li>
      <li><span>Hardware Install</span><span class="rate">$100/hr</span></li>
      <li><span>Phone Setup &amp; Configuration</span><span class="rate">$100/hr</span></li>
      <li><span>Home Entertainment Ins</span><span class="rate">$100/hr</span></li>
      <li><span>Tv &amp; Display Install &amp; Mounting</span><span class="rate">$100/hr</span></li>
      <li><span>On-site Troubleshooting</span><span class="rate">$100/hr</span></li>
      <li><span>Printer Setup</span><span class="rate">$100/hr</span></li>
      <li><span>Data Backup</span><span class="rate">$100/hr</span></li>
      <li><span>Computer Setup</span><span class="rate">$100/hr</span></li>
      <li><span>Software Install</span><span class="rate">$100/hr</span></li>
      <li><span>Data Recovery</span><span class="rate">$100/hr</span></li>
    </ul>
  </article>

  <article class="panel panel--business">
    <h2 class="heading"><span class="top">BUSINESS</span><span class="bottom">SERVICES</span></h2>
    <p class="intro">BDP aims to help small businesses thrive by managing the technical aspects so they can focus on what they do best. We offer various services and are happy to travel on-site to CT, RI and MA to provide them. Our premier business service is managed IT, one multiple businesses within the RI area have subscribed to to keep everything working flawlessly.</p>
    <ul class="price-list">
      <li><span>Email Setup (business)</span><span class="rate">$100/hr</span></li>
      <li><span>Virus Removal (business)</span><span class="rate">$100/hr</span></li>
      <li><span>Tune Up (business)</span><span class="rate">$100/hr</span></li>
      <li><span>Computer Setup (business)</span><span class="rate">$100/hr</span></li>
      <li><span>Data Backup (business)</span><span class="rate">$100/hr</span></li>
      <li><span>Printer Setup (business)</span><span class="rate">$100/hr</span></li>
      <li><span>Data Recovery (business)</span><span class="rate">$100/hr</span></li>
      <li><span>Phone Setup &amp; Configuration</span><span class="rate">$100/hr</span></li>
      <li><span>Software Install (business)</span><span class="rate">$100/hr</span></li>
      <li><span>Managed It Services</span><span class="rate">$100/hr</span></li>
      <li><span>On-site Troubleshoot</span><span class="rate">$100/hr</span></li>
      <li><span>Graphic Design</span><span class="rate">$100/hr</span></li>
      <li><span>Server Configuration</span><span class="rate">$100/hr</span></li>
      <li><span>Wifi/wired Network Install &amp; Setup</span><span class="rate">$100/hr</span></li>
      <li><span>Office Setup</span><span class="rate">$100/hr</span></li>
    </ul>
  </article>

  <article class="panel panel--web">
    <h2 class="heading"><span class="top">WEB</span><span class="bottom">SERVICES</span></h2>
    <p class="intro">We have the experience and knowledge to improve your business with a brand new website or provide a revamp of it's design to bring it to an even more attractive and modern form. All of our in-house built websites are built to be mobile compatible, search engine optimized, and styled uniquely to your design preferences. We never outsource our projects, and we build every website uniquely for each client.</p>
    <p class="intro">In addition to website creation, we handle all facets of web services, including website content updates, web hosting and email services and much more. We work to offer fair price and quality of service that is above the rest, while providing exactly what the client needs. We will quote you for something your business needs, and are here to help get things rolling from day one, with free consultations so you know how we can grow your business.</p>
    <p class="intro">All of our websites are protected by Skyshield protection for even more benefit, along with secure premium email hosting for every client.</p>
  </article>

  <footer class="clients">
    <span class="clients-tab">Our Clients</span>
    <ul class="client-names">
      <li>Tallis Transit</li><li>Trailmark Youth</li><li>Oakline Homes</li><li>Paws Forward</li><li>Redbird Motors</li><li>Harborview Realty</li><li>Meridian Planning Group</li><li>Corvo Media</li><li>Kestrel Realty</li><li>Glue &amp; Grit</li><li>Pine Ridge Group</li>
    </ul>
  </footer>
</section>

<section class="cover">
  <div class="brand">
    <div class="brand-mark">BDP</div>
    <div class="brand-name">Bluerock Data Partners</div>
  </div>
  <div class="cover-photo" role="img" aria-label="Photo of two technicians working on a laptop in a server room"></div>
  <h1 class="cover-title"><span>HOME</span><span class="mid">AND BUSINESS</span><span>IT SERVICES</span></h1>
  <p class="cover-sub">SOFTWARE SERVICE<br>WEB SOLUTION</p>
  <div class="cover-rule"></div>
  <p class="cover-url">www.<b>BluerockData</b>.partners</p>
</section>

</body>
</html>
```